Book Cover Design GML

Want a new book cover but want to use the same photo and change the sub name. This is for a brand called "Golden Maple Living". The book is called "Just Steps, Just Results"

This is for a 8.5 * 11 book size

We really want to brand the Golden Maple Living

I've attached a sample of an old book cover, the photo I want used and the golden maple living logo

Requirements
Must have
• Must have the logo,

must have the book title. "Just Steps, Just Results"

Must have "Featuring" The Golden Maple Living Fit Roll Card Game"

On the back put the logo and Golden Maple Living Nutrition

must have the authors name "Dana Holcomb" on the page

"The Prime Shape Roadmap"
Nice to have
• Golden Maple Living Presents:

the book title

```html
<!DOCTYPE html>
<html lang="en">
<head>
<meta charset="utf-8">
<title>Just Steps, Just Results — Golden Maple Living</title>
<link rel="stylesheet" href="https://fonts.googleapis.com/css2?family=Open+Sans:wght@400;600;700&family=Raleway:wght@200&display=swap">
<style>
  :root {
    --backdrop: #e9e9e9;
    --cover: #121212;
    --teal: #6fd8c6;
    --white: #ffffff;
    --muted: #cfcfcf;
  }
  * { margin: 0; padding: 0; box-sizing: border-box; }
  html, body {
    width: 1200px;
    height: 862px;
    overflow: hidden;
    background: var(--backdrop);
  }
  .book-cover {
    position: absolute;
    left: 282px;
    top: 20px;
    width: 635px;
    height: 822px;
    background: var(--cover);
    overflow: hidden;
  }
  .cover-art {
    position: absolute;
    inset: 0;
    width: 100%;
    height: 100%;
  }
  .presents {
    font-family: "Open Sans", sans-serif;
    font-weight: 400;
    font-size: 9.5px;
    fill: var(--teal);
  }
  .title-large,
  .title-thin {
    font-family: "Raleway", sans-serif;
    font-weight: 200;
    fill: var(--teal);
  }
  .title-bold {
    font-family: "Open Sans", sans-serif;
    font-weight: 700;
    fill: var(--teal);
  }
  .roadmap {
    font-family: "Open Sans", sans-serif;
    font-weight: 600;
    font-size: 13px;
    letter-spacing: 1.5px;
    fill: var(--teal);
  }
  .featuring {
    font-family: "Open Sans", sans-serif;
    font-weight: 400;
    font-size: 10.5px;
    fill: var(--muted);
  }
  .brand {
    position: absolute;
    left: 150px;
    top: 652px;
    display: flex;
    align-items: center;
    gap: 14px;
  }
  .brand-mark {
    width: 40px;
    height: 40px;
    background: var(--white);
  }
  .brand-name {
    display: flex;
    flex-direction: column;
    gap: 3px;
    font-family: "Open Sans", sans-serif;
    font-weight: 600;
    color: var(--white);
    text-transform: uppercase;
    line-height: 1;
  }
  .brand-line-main { font-size: 18px; letter-spacing: 2px; }
  .brand-line-sub { font-size: 10px; letter-spacing: 6px; }
  .brand-line-tag { font-size: 6.5px; letter-spacing: 1.5px; }
  .author {
    position: absolute;
    left: 0;
    right: 0;
    top: 758px;
    text-align: center;
    font-family: "Open Sans", sans-serif;
    font-weight: 600;
    font-size: 14px;
    letter-spacing: 4px;
    color: var(--white);
    text-transform: uppercase;
  }
</style>
</head>
<body>
  <main class="book-cover">
    <svg class="cover-art" viewBox="0 0 635 822" xmlns="http://www.w3.org/2000/svg">
      <defs>
        <linearGradient id="portrait-tone" x1="0" y1="0" x2="1" y2="1">
          <stop offset="0" stop-color="#3a2a22"/>
          <stop offset="0.45" stop-color="#4fbfae"/>
          <stop offset="1" stop-color="#1b1b24"/>
        </linearGradient>
      </defs>

      <text class="presents" x="414" y="352" text-anchor="end">Golden Maple Living Presents:</text>

      <text class="title-large" x="2" y="466" font-size="120" textLength="220" lengthAdjust="spacingAndGlyphs">JUST</text>
      <text class="title-thin" x="230" y="420" font-size="56" textLength="184" lengthAdjust="spacingAndGlyphs">STEPS,</text>
      <text class="title-bold" x="231" y="464" font-size="40" textLength="183" lengthAdjust="spacingAndGlyphs">RESULTS</text>

      <text class="roadmap" x="2" y="500">THE PRIME SHAPE ROADMAP</text>
      <text class="featuring" x="2" y="520">Featuring The Golden Maple Living Fit Roll Card Game</text>

      <rect x="420" y="265" width="200" height="240" rx="4" fill="url(#portrait-tone)"
            role="img" aria-label="Photo of the author in workout wear leaning on a teal exercise ball"/>
    </svg>

    <div class="brand">
      <span class="brand-mark"></span>
      <span class="brand-name">
        <span class="brand-line-main">Golden Maple</span>
        <span class="brand-line-sub">Living</span>
        <span class="brand-line-tag">Nutrition</span>
      </span>
    </div>

    <p class="author">Dana Holcomb</p>
  </main>
</body>
</html>
```